Gardowell - Direct Mail DL flyer design

Create a direct market flyer (d/l size) to compel people to act and visit our website to buy life insurance.

Copy, example images and notes are provided

Target Market(s)

Families with debt who need life insurance

Industry/Entity Type

Insurance

Requirements
Must have
• Our logo
• Colours are Blue C99, M79, Y0, K0 Green C40, M0, Y100, K0
• Copy side 1 is "For the price of a coffee you can ensure you and your family get the right start."
• Copy side 2 is "It doesn't sound like much, but when it comes to life insurance, $1 a day* can make a huge difference if you were to die.
• For the cost of a cup of coffee a day, you can ensure your family will be left with enough to protect the home, pay for ongoing living expenses and fund your children's continued education.
• Your life is important
• Apply today and get 1 month free cover
• Build your tomorrow
• company logo gardowell.com.au make prominant
• *For a monthly premium of $25.33, a 35 year old non-smoking male can obtain $300,000 of term life cover.
• Example for illistration purpose only. The premium cited is current as at February 2016, is based on the factors referred to in the example and subject to underwriting. You should consider whether this product is appropriate for you. Refer to the Product Disclosure Statement, available from gardowell before deciding whether to acquire the product."
• Footer
• Gardowell Pty Ltd
• ABN 47 253 918 604 AFS Licence 729140
Nice to have
• Coffee cup with pods/capsuals around it white background side 1 and coffee ring stain on reverse as watermark
• Trusafe has been awarded - Merrow Ratings - 2014 Kestrel Protection Honours for Term Cover
• Trusafe has been awarded - Merrow Ratings - 2015 Kestrel Protection Honours for Term Cover

```html
<!DOCTYPE html>
<html lang="en">
<head>
<meta charset="utf-8">
<title>Gardowell – DL Flyer</title>
<link rel="stylesheet" href="https://fonts.googleapis.com/css2?family=Alfa+Slab+One&family=Open+Sans:wght@400&display=swap">
<style>
  :root {
    --brand-blue: #1f3f93;
    --brand-green: #8dc63f;
    --ink-shadow: #0d1a3a;
    --coffee-dark: #3a2417;
    --coffee-mid: #6b4630;
    --paper: #ffffff;
  }
  * { margin: 0; padding: 0; box-sizing: border-box; }
  html, body { width: 1200px; height: 2398px; overflow: hidden; background: var(--paper); }
  .flyer { position: relative; width: 1200px; height: 2398px; background: var(--paper); overflow: hidden; }
  .corner-shape { position: absolute; left: 0; top: 0; }
  .headline {
    position: absolute; left: 155px; top: 62px; width: 1000px;
    font-family: "Alfa Slab One", Georgia, serif;
    font-weight: 400;
    font-size: 98px; line-height: 113px;
    color: var(--brand-blue);
    text-shadow: 4px 5px 0 var(--ink-shadow);
    white-space: nowrap;
  }
  .rule { position: absolute; left: 0; width: 1200px; }
  .rule--green-top { top: 663px; height: 17px; background: var(--brand-green); }
  .rule--blue-top { top: 698px; height: 18px; background: var(--brand-blue); }
  .rule--blue-bottom { top: 1866px; height: 18px; background: var(--brand-blue); }
  .rule--green-bottom { top: 1901px; height: 20px; background: var(--brand-green); }
  .hero-photo {
    position: absolute; left: 0; top: 903px; width: 1200px; height: 714px;
    background: radial-gradient(ellipse at 45% 55%, var(--coffee-mid) 0%, var(--coffee-dark) 75%);
  }
  .brand__mark {
    position: absolute; left: 70px; top: 2103px;
    width: 162px; height: 180px; border-radius: 22px; background: var(--brand-green);
  }
  .brand__name {
    position: absolute; left: 257px; top: 2098px;
    font-family: "Open Sans", Arial, sans-serif;
    font-weight: 400; font-size: 82px; line-height: 1;
    color: var(--brand-blue);
    white-space: nowrap;
  }
  .brand__tagline {
    position: absolute; right: 227px; top: 2206px;
    font-family: "Open Sans", Arial, sans-serif;
    font-weight: 400; font-size: 38px; line-height: 1;
    letter-spacing: 5px; color: var(--brand-blue);
    white-space: nowrap;
  }
</style>
</head>
<body>
<main class="flyer">
  <svg class="corner-shape" width="1200" height="2398" viewBox="0 0 1200 2398" aria-hidden="true">
    <path d="M0 0 H324 C180 150 40 380 0 661 Z" fill="var(--brand-green)"/>
    <path d="M1200 1921 H1173 C1100 2080 960 2270 886 2398 H1200 Z" fill="var(--brand-blue)"/>
  </svg>

  <h1 class="headline">For the price of a<br>coffee you can<br>ensure you and<br>your family get<br>the right start.</h1>

  <div class="rule rule--green-top"></div>
  <div class="rule rule--blue-top"></div>

  <div class="hero-photo" role="img" aria-label="Cup of espresso and coffee capsules resting on a bed of roasted coffee beans"></div>

  <div class="rule rule--blue-bottom"></div>
  <div class="rule rule--green-bottom"></div>

  <div class="brand__mark" aria-hidden="true"></div>
  <span class="brand__name">gardowell.com.au</span>
  <span class="brand__tagline">build your tomorrow</span>
</main>
</body>
</html>
```